Business card design Needed for new logo / Construction business, home extensions and new builds

We need a business card design using our new logo files which i will attach to this project :)

We are a small construction business specialising in home extensions, new builds and property development. We are very ambitious and would appreciate professional and elegant designs for our new business card.

Very serious about using the services on BriefNest and recently acquired our new logo from here :)

Please get involved, i will feedback when i can as i am very busy but can respond daily, thanks

Target Market(s)

People that want to build onto their houses, new building developments or adding too their existing property

Industry/Entity Type

Construction

Contact Information for Business Card

Hollin Marsh Construction, Tobias Renwick (Managing Director), Tel 07822200444, email - info@hollin-marsh, www.hollin-marsh.co.uk

Colors

Designer to choose colors to be used in the design.

Requirements
Must have
• I like a deep grey on the back please. A lot of you have provided black from and back, try mixing things up a little. The black looks cool 😎 Thanks

```html
<!DOCTYPE html>
<html lang="en">
<head>
<meta charset="utf-8">
<title>Hollin Marsh Construction – Business Card</title>
<link href="https://fonts.googleapis.com/css2?family=Montserrat:wght@400;500;600&display=swap" rel="stylesheet">
<style>
  :root {
    --stage: #5a5d61;
    --card-front: #231f20;
    --card-back: #3a3b3f;
    --gold: #d9a53a;
    --gold-light: #f3cf6f;
    --silver: #d6d8da;
    --text: #e8e8e8;
  }
  * { box-sizing: border-box; margin: 0; padding: 0; }
  html, body { width: 1200px; height: 895px; overflow: hidden; }
  body {
    background: var(--stage);
    font-family: "Montserrat", sans-serif;
    display: flex;
    align-items: center;
    justify-content: center;
    gap: 44px;
  }
  .card {
    position: relative;
    width: 530px;
    height: 303px;
    box-shadow: 0 12px 30px rgba(0,0,0,.45);
    overflow: hidden;
  }
  .card--front { background: var(--card-front); }
  .card--back { background: var(--card-back); }
  .card__edge {
    position: absolute;
    left: 0; right: 0; bottom: 0;
    height: 5px;
    background: linear-gradient(90deg, var(--gold), var(--gold-light), var(--gold));
  }
  .brand {
    display: flex;
    align-items: center;
    gap: 10px;
    color: var(--gold);
    font-weight: 500;
    text-transform: uppercase;
  }
  .brand__mark {
    width: 14px; height: 14px;
    background: var(--gold);
    flex: none;
  }
  .brand__name { font-size: 19px; letter-spacing: 2px; line-height: 1.35; }
  .card--front {
    display: flex;
    align-items: center;
    justify-content: center;
  }
  .card--back .brand {
    position: absolute;
    left: 44px;
    top: 50%;
    transform: translateY(-50%);
  }
  .card--back .brand__name { font-size: 16px; }
  .divider {
    position: absolute;
    left: 270px;
    top: 72px;
    width: 1.5px;
    height: 150px;
    background: var(--gold);
  }
  .contact {
    position: absolute;
    left: 300px;
    top: 82px;
    color: var(--text);
  }
  .contact__name {
    font-size: 19px;
    font-weight: 600;
    letter-spacing: .5px;
    color: var(--silver);
  }
  .contact__role { font-size: 10px; margin-top: 2px; }
  .contact__list { list-style: none; margin-top: 22px; }
  .contact__item {
    display: flex;
    align-items: center;
    gap: 10px;
    font-size: 11px;
    margin-bottom: 10px;
  }
  .contact__icon { width: 15px; height: 15px; flex: none; fill: var(--gold); }
</style>
</head>
<body>
  <section class="card card--front">
    <div class="brand">
      <span class="brand__mark"></span>
      <span class="brand__name">Hollin Marsh<br>Construction</span>
    </div>
    <div class="card__edge"></div>
  </section>

  <section class="card card--back">
    <div class="brand">
      <span class="brand__mark"></span>
      <span class="brand__name">Hollin Marsh<br>Construction</span>
    </div>
    <div class="divider"></div>
    <div class="contact">
      <p class="contact__name">TOBIAS RENWICK</p>
      <p class="contact__role">Managing Director</p>
      <ul class="contact__list">
        <li class="contact__item">
          <svg class="contact__icon" viewBox="0 0 24 24"><path d="M6.6 10.8c1.4 2.8 3.8 5.1 6.6 6.6l2.2-2.2c.3-.3.7-.4 1-.2 1.1.4 2.3.6 3.6.6.6 0 1 .4 1 1V20c0 .6-.4 1-1 1C10.6 21 3 13.4 3 4c0-.6.4-1 1-1h3.5c.6 0 1 .4 1 1 0 1.3.2 2.5.6 3.6.1.3 0 .7-.2 1z"/></svg>
          07822200444
        </li>
        <li class="contact__item">
          <svg class="contact__icon" viewBox="0 0 24 24"><path d="M2 5h20v14H2z M4 7v.4l8 5.2 8-5.2V7z" fill-rule="evenodd"/></svg>
          info@hollin-marsh
        </li>
        <li class="contact__item">
          <svg class="contact__icon" viewBox="0 0 24 24"><circle cx="12" cy="12" r="10" fill="none" stroke="#d9a53a" stroke-width="2"/><path d="M2 12h20M12 2c3 3 3 17 0 20M12 2c-3 3-3 17 0 20" fill="none" stroke="#d9a53a" stroke-width="1.6"/></svg>
          www.hollin-marsh.co.uk
        </li>
      </ul>
    </div>
    <div class="card__edge"></div>
  </section>
</body>
</html>
```